The Copper Lantern Business Cards

We are a Craft Beer/Upscale dining Bar/Restaurant. We'll have 24 taps of craft beers and several types of bottled beers. In addition, we'll be serving a variety of top shelf bourbons, spirits and wines with a small unique menu. I'd like the design to be sophisticated, elegant and modern while staying away from "cartoonish" pictures.
Updates
Hello, I've added some example logos for inspiration. I'd like to use a lot of black/white with maybe a little color for a "pop". Thank you!
Industry/Entity Type
Business
Contact Information for Business Card
THE COPPER LANTERN
Marco Dellarosa
592 Wexley Street
Norfolk, Virginia 23847
Office: (757) 555-0148
Mobile: (757) 555-0193
Look and feel

```html
<!DOCTYPE html>
<html lang="en">
<head>
<meta charset="UTF-8">
<title>The Copper Lantern – Business Card</title>
<link rel="stylesheet" href="https://fonts.googleapis.com/css2?family=Lato:wght@400;700&display=swap">
<style>
  :root {
    --page-bg: #e9e6e1;
    --card-black: #111111;
    --card-black-edge: #1b1b1b;
    --accent-orange: #ef5416;
    --text-white: #f2f2f2;
    --band-light: #d9d9d9;
    --address-bg: #e4e4e4;
  }
  * { margin: 0; padding: 0; box-sizing: border-box; }
  html, body {
    width: 1200px;
    height: 900px;
    overflow: hidden;
    background: var(--page-bg);
    font-family: "Lato", sans-serif;
  }
  .business-card {
    position: absolute;
    left: 75px;
    top: 150px;
    width: 1050px;
    height: 600px;
    background: radial-gradient(ellipse at 40% 30%, var(--card-black-edge), var(--card-black) 70%);
    overflow: hidden;
    box-shadow: 0 14px 40px rgba(0,0,0,0.28);
  }
  .card-wave {
    position: absolute;
    inset: 0;
    width: 100%;
    height: 100%;
  }
  .brand-name {
    position: absolute;
    left: 140px;
    top: 62px;
    font-size: 74px;
    font-weight: 400;
    letter-spacing: 1px;
    color: var(--text-white);
    white-space: nowrap;
  }
  .tagline {
    position: absolute;
    left: 150px;
    top: 170px;
    font-size: 24px;
    letter-spacing: 2px;
    color: var(--text-white);
    white-space: nowrap;
  }
  .tagline .dot { color: var(--accent-orange); margin: 0 12px; }
  .address-bar {
    position: absolute;
    left: 150px;
    top: 218px;
    padding: 8px 26px;
    background: var(--address-bg);
    color: var(--accent-orange);
    font-size: 26px;
    font-weight: 700;
    white-space: nowrap;
  }
  .contact-name {
    position: absolute;
    left: 290px;
    top: 300px;
    font-size: 32px;
    font-weight: 700;
    letter-spacing: 1px;
    color: var(--accent-orange);
  }
  .phone-line {
    position: absolute;
    font-size: 28px;
    white-space: nowrap;
  }
  .phone-line .label { color: var(--accent-orange); margin-right: 26px; }
  .phone-line .number { color: var(--text-white); }
  .phone-mobile { left: 630px; top: 302px; }
  .phone-office { left: 110px; top: 392px; }
</style>
</head>
<body>
  <div class="business-card">
    <svg class="card-wave" viewBox="0 0 1050 600" preserveAspectRatio="none" aria-hidden="true">
      <path d="M0 440 C 220 480, 500 450, 700 400 C 850 362, 950 330, 1050 295 L1050 600 L0 600 Z" fill="var(--band-light)"/>
      <path d="M0 500 C 260 530, 540 490, 740 430 C 870 390, 970 350, 1050 320 L1050 600 L0 600 Z" fill="var(--accent-orange)"/>
    </svg>

    <div class="brand-name">THE COPPER LANTERN</div>
    <div class="tagline">CRAFT BEER<span class="dot">•</span>UPSCALE DINING BAR<span class="dot">•</span>RESTAURANT</div>
    <div class="address-bar">592 Wexley Street Norfolk, Virginia 23847</div>

    <div class="contact-name">MARCO DELLAROSA</div>
    <div class="phone-line phone-mobile"><span class="label">Mobile :</span><span class="number">(757) 555-0193</span></div>
    <div class="phone-line phone-office"><span class="label">Office :</span><span class="number">(757) 555-0148</span></div>
  </div>
</body>
</html>
```